Revise Three Graphics for Company Careers website.

We have a need to find an alternative artistic approach to revising three graphics currently used on a growing companies careers/job website.
- The new art for attached graphics (named graphic #1, #2, and #3) should be clean, professional and easy to read.
- The art representing these three pieces should share common artistic elements and not necessarily look like three differently branded pieces.
- The careers site is shared between two related companies, so the colors used should complement the colors of two companies (whose logos are attached).
- Logos can be used as knock-outs if needed.
Note: Graphic #3 (currently a set of boxes 2x3) needs two additional boxes with the following copy:
- Art and Science of Communication
- Supervising 101
Lastly, Graphic #4 we need to be put into the same color font used in the two company logos. That's it!

```html
<!DOCTYPE html>
<html lang="en">
<head>
<meta charset="utf-8">
<title>Careers – Training and Development</title>
<link rel="stylesheet" href="https://fonts.googleapis.com/css2?family=Arimo:wght@700&display=swap">
<style>
  :root {
    --bg: #ffffff;
    --label: #8d8d8d;
    --brand-navy: #1f3f7a;
    --brand-blue: #2a6fb0;
    --brand-dot: #9bb823;

    --yellow: #f7c71b;
    --gold: #f5b016;
    --orange: #ec7a3c;
    --red: #d8283e;
    --green: #6e9a2b;
    --lime: #9bb823;
    --blue: #2b9ad8;
    --cyan: #2aaae2;
    --navy: #15416f;
    --teal: #6ea89d;
    --sage: #8fbea6;
  }
  * { margin: 0; padding: 0; box-sizing: border-box; }
  html, body { width: 1200px; height: 927px; overflow: hidden; background: var(--bg); }
  .canvas {
    position: relative;
    width: 1200px;
    height: 927px;
    background: var(--bg);
    font-family: "Arimo", Arial, sans-serif;
  }

  .topic {
    position: absolute;
    font-weight: 700;
    font-size: 21px;
    line-height: 26px;
    color: var(--label);
    letter-spacing: -0.2px;
    white-space: nowrap;
  }

  .motif {
    position: absolute;
    width: 282px;
    height: 285px;
  }
  .motif--warm   { left: 63px;  top: 432px; background: linear-gradient(135deg, var(--yellow), var(--orange) 45%, var(--red) 70%, var(--gold)); }
  .motif--cool   { left: 323px; top: 345px; background: linear-gradient(135deg, var(--green), var(--blue) 45%, var(--navy) 70%, var(--teal)); }
  .motif--sunset { left: 585px; top: 254px; background: linear-gradient(135deg, var(--orange), var(--red) 45%, var(--gold) 70%, var(--green)); }
  .motif--fresh  { left: 845px; top: 165px; background: linear-gradient(135deg, var(--sage), var(--navy) 45%, var(--lime) 70%, var(--cyan)); }

  .brand {
    position: absolute;
    font-weight: 700;
    white-space: nowrap;
  }
  .brand--primary { left: 52px; top: 46px; font-size: 30px; color: var(--brand-navy); letter-spacing: 0.5px; }
  .brand--partner {
    right: 50px; bottom: 62px; font-size: 30px; color: var(--brand-blue);
    display: flex; align-items: center; gap: 12px;
  }
  .brand-dot { width: 16px; height: 16px; border-radius: 50%; background: var(--brand-dot); }
</style>
</head>
<body>
<main class="canvas">
  <div class="brand brand--primary">CORVANA TECHNOLOGIES</div>

  <div class="motif motif--warm" role="img" aria-label="Geometric pinwheel of yellow, orange and red triangles"></div>
  <div class="motif motif--cool" role="img" aria-label="Geometric pinwheel of green, blue, navy and teal triangles"></div>
  <div class="motif motif--sunset" role="img" aria-label="Geometric pinwheel of orange, red, gold and green triangles"></div>
  <div class="motif motif--fresh" role="img" aria-label="Geometric pinwheel of sage, navy, lime and cyan triangles"></div>

  <p class="topic" style="left:78px; top:353px;">Scientific Lunch<br>and Learns</p>
  <p class="topic" style="left:78px; top:739px;">Statistics in Pharmaceutical<br>Development Workshop</p>
  <p class="topic" style="left:409px; top:264px;">Conferences<br>and Seminars</p>
  <p class="topic" style="left:409px; top:652px;">Leadership<br>Development</p>
  <p class="topic" style="left:652px; top:184px;">Creating the Right<br>Team Workshop</p>
  <p class="topic" style="left:652px; top:559px;">Project Management<br>Training</p>
  <p class="topic" style="left:921px; top:98px;">Art and Science<br>of Communication</p>
  <p class="topic" style="left:913px; top:473px;">Supervising 101</p>

  <div class="brand brand--partner"><span class="brand-dot"></span>meridel therapeutics</div>
</main>
</body>
</html>
```